Revamp my web site design

Willowmere Care Practitioners is a not for profit organisation focused on providing emotional support and counselling services to those with cancer or affected by cancer including those bereaved.

Our web site is intended to welcome suffers to engage with the services of its members and is also provided to encourage additional counsellors to join the organisation and then supports its members with access to materials and courses to extend their professional development.

We have a limited budget and seek to not only improve the attractiveness of the site but also improve the functionality and ease of maintenance. Especially site administrtaion should allow for uploading documents, adding new members, news and events easily.

Existing site is www.brightharbourcare.com.au

```html
<!DOCTYPE html>
<html lang="en">
<head>
<meta charset="utf-8">
<title>Willowmere Care Practitioners</title>
<link href="https://fonts.googleapis.com/css2?family=Signika:wght@300;400;600&display=swap" rel="stylesheet">
<style>
:root{
  --page-bg:#eeeeee;
  --paper:#ffffff;
  --ink:#333333;
  --muted:#555555;
  --blue:#1f7fb8;
  --red:#b5212a;
  --green:#4f8a10;
  --orange:#d9870f;
  --nav-dark:#2a2a2a;
  --nav-line:#444444;
  --frame:#cfcfcf;
  --panel:#f4f4f4;
  --footer:#4b4a4b;
  --footer-bottom:#232323;
  --footer-text:#e6e6e6;
}
*{box-sizing:border-box;margin:0;padding:0}
html,body{width:900px;height:1200px;overflow:hidden}
body{background:var(--page-bg);font-family:"Signika",sans-serif;font-weight:300;color:var(--ink);position:relative}
.page{position:absolute;left:67px;top:0;width:765px;height:1200px;background:var(--paper)}
.abs{position:absolute}

.brand{left:77px;top:12px;width:190px}
.brand-mark{position:absolute;left:47px;top:0;width:96px;height:96px;border-radius:50%;background:#e9eef2}
.brand-name{position:absolute;left:0;top:106px;font-size:25px;font-weight:400;color:#333;white-space:nowrap}

.utility{right:76px;top:19px;font-size:11px;font-weight:400;color:#444}
.utility a{color:var(--blue);text-decoration:none}
.utility .sep{color:#777;margin:0 6px}

.search{left:618px;top:48px;width:206px;height:28px;border:1px solid #d4d4d4;background:#fff;box-shadow:inset 0 1px 2px rgba(0,0,0,.08)}
.search-placeholder{position:absolute;left:14px;top:6px;font-size:11px;color:#888}
.search-btn{position:absolute;right:4px;top:4px;width:19px;height:18px;background:#bcbcbc;border-radius:2px}

.nav{left:329px;top:114px;width:496px;height:38px;background:linear-gradient(#3b3b3b,#1d1d1d);display:flex;border-radius:2px}
.nav a{color:#f2f2f2;font-size:12px;font-weight:300;text-decoration:none;display:flex;align-items:center;justify-content:center;border-right:1px solid var(--nav-line)}
.nav a.active{color:#f3a43a}
.nav a:last-child{border-right:0}

.hero{left:74px;top:168px;width:751px;height:264px;border:4px solid var(--frame);background:linear-gradient(90deg,#e4e2e8 0%,#d8d6de 100%)}
.hero-photo{position:absolute;left:0;top:0;width:342px;height:256px;background:linear-gradient(120deg,#8d7a68 0%,#c9b59c 45%,#e9e4df 100%)}
.hero-title{position:absolute;left:430px;top:22px;width:300px;font-size:17px;font-weight:400;line-height:24px;color:#2e2e2e}
.finder{position:absolute;left:427px;top:79px;width:298px;height:122px;background:#9a999c;border-radius:2px}
.finder h2{position:absolute;left:10px;top:10px;font-size:17px;font-weight:400;color:#fff}
.field{position:absolute;background:#fff;border:1px solid #ddd;font-size:10.5px;font-weight:300;color:#777;padding:7px 14px;height:28px;left:10px;width:245px}
.field.location{top:44px}
.field.zip{top:81px}
.field.location svg{position:absolute;right:10px;top:10px}
.go{position:absolute;left:260px;top:81px;width:32px;height:28px;background:#333;color:#fff;font-size:13px;font-weight:400;display:flex;align-items:center;justify-content:center;border-radius:2px}
.dots{position:absolute;left:666px;top:234px;display:flex;gap:8px}
.dots i{width:10px;height:10px;border-radius:50%;background:#8d8c90;display:block}
.dots i:first-child{background:#333}

.welcome{left:76px;top:452px;width:530px}
.welcome h1{font-size:17px;font-weight:400;color:var(--red);margin-bottom:10px}
.welcome p{font-size:11.2px;line-height:18.8px;color:#333;font-weight:300;letter-spacing:-.2px}
.btn-more{left:76px;top:602px;width:78px;height:28px;background:linear-gradient(#4a4a4a,#222);color:#fff;font-size:11.5px;font-weight:400;border-radius:2px;display:flex;align-items:center;justify-content:center}
.divider{left:76px;top:654px;width:530px;height:1px;background:#dcdcdc}

.feature h3{position:absolute;font-size:17px;font-weight:400;color:var(--blue);white-space:nowrap}
.feature .thumb{position:absolute;width:260px;height:125px;border:3px solid var(--frame)}
.thumb.a{background:linear-gradient(120deg,#ececec,#a7a19b 55%,#dfe3e6)}
.thumb.b{background:linear-gradient(90deg,#e9e6e0,#cdb8a4 50%,#d66c55 80%,#eaeaea)}
.thumb.c{background:linear-gradient(160deg,#3d6fae,#c9d4e4 45%,#d99a84 70%,#6a8fc4)}
.thumb.d{background:radial-gradient(ellipse at 55% 60%,#c79a73 0%,#e6dcd2 40%,#ffffff 75%)}

.side h2{position:absolute;font-size:17px;font-weight:400;color:var(--green)}
.side-box{position:absolute;left:626px;width:200px;border:2px solid #eeeeee;background:#fff}
.side-box ul{list-style:none;padding:18px 8px 0 18px}
.side-box li{position:relative;padding-left:12px;font-size:10.5px;font-weight:300;line-height:16px;color:#333;margin-bottom:13px}
.side-box li::before{content:"";position:absolute;left:0;top:5px;border-left:4px solid #777;border-top:3px solid transparent;border-bottom:3px solid transparent}
.side-box time{display:block;color:var(--orange);font-size:10.5px;margin-top:2px}
.view-all{position:absolute;left:0;bottom:0;width:100%;height:36px;background:var(--panel);color:var(--green);font-size:11.5px;font-weight:400;padding:10px 0 0 16px}

.footer{left:74px;top:1027px;width:752px;height:131px;background:var(--footer)}
.footer-col{position:absolute;top:16px;color:var(--footer-text)}
.footer-col h4{font-size:11px;font-weight:300;margin-bottom:10px}
.footer-col li{list-style:none;font-size:10.5px;font-weight:300;margin-bottom:6px;color:#d6d6d6}
.footer-col li::before{content:"» ";}
.email{position:absolute;left:572px;top:43px;width:162px;height:28px;background:#fff;border:1px solid #ccc;font-size:10.5px;font-weight:300;color:#777;padding:7px 15px}
.email .arrow{position:absolute;right:4px;top:3px;width:20px;height:20px;border-radius:50%;background:#eee;border:1px solid #bbb}
.email .arrow svg{position:absolute;left:-1px;top:-1px}
.social{position:absolute;top:85px;left:592px;display:flex;gap:6px}
.social i{display:block;width:28px;height:28px;border-radius:50%;border:2px solid #fff}
.social .s1{background:#3b5998}.social .s2{background:#2aa9e0}.social .s3{background:#0e76a8}.social .s4{background:#f7931e}
.copyright{left:74px;top:1158px;width:752px;height:42px;background:var(--footer-bottom);color:#ddd;font-size:11px;font-weight:300;display:flex;align-items:center;justify-content:center}
</style>
</head>
<body>
<div class="page"></div>

<div class="abs brand">
  <span class="brand-mark"></span>
  <span class="brand-name">Willowmere Care</span>
</div>

<div class="abs utility">Call us : 555 014 2290<span class="sep">|</span><a href="#">Register</a><span class="sep">|</span><a href="#">Login</a></div>

<div class="abs search"><span class="search-placeholder">Search</span><span class="search-btn"><svg width="19" height="18" viewBox="0 0 19 18"><circle cx="8.5" cy="8" r="4" fill="none" stroke="#fff" stroke-width="1.6"/><line x1="11.5" y1="11" x2="14.5" y2="14" stroke="#fff" stroke-width="1.8"/></svg></span></div>

<nav class="abs nav">
  <a class="active" href="#" style="width:63px">Home</a>
  <a href="#" style="width:82px">Contact Us</a>
  <a href="#" style="width:99px">News &amp; Events</a>
  <a href="#" style="width:64px">Articles</a>
  <a href="#" style="width:113px">Find a Counsellor</a>
  <a href="#" style="width:75px">Members</a>
</nav>

<section class="abs hero">
  <div class="hero-photo" role="img" aria-label="Photo of a counsellor comforting a smiling elderly man with a walking cane"></div>
  <p class="hero-title">A diagnosis of cancer is a devastating experience for most people.</p>
  <div class="finder">
    <h2>Find A Counsellor</h2>
    <div class="field location">Search by Location<svg width="12" height="8" viewBox="0 0 12 8"><path d="M0 0h12L6 8z" fill="#888"/></svg></div>
    <div class="field zip">Enter your Zip code</div>
    <div class="go">Go</div>
  </div>
  <div class="dots"><i></i><i></i><i></i><i></i></div>
</section>

<section class="abs welcome">
  <h1>Welcome to Willowmere Care Practitioners&nbsp; Inc</h1>
  <p>Many people can get support by talking to close family or friends. However, it can sometimes help to talk to someone from outside of that circle who has been trained to listen and help you explore your feelings.&nbsp; You may feel as if you are riding an emotional rollercoaster. Often talking of your distress to those close to you can be difficult and painful. When someone is diagnosed with cancer, they and their family can feel shocked, numb, directionless and afraid. They often feel they need to talk things through in confidence with someone who understands the emotional challenges of cancer.</p>
</section>
<div class="abs btn-more">Know more</div>
<div class="abs divider"></div>

<div class="feature">
  <h3 style="left:75px;top:667px">What is counselling?</h3>
  <div class="thumb a" style="left:74px;top:697px" role="img" aria-label="Photo of a father talking with his young son on a sofa"></div>
  <h3 style="left:347px;top:667px">Why cancer counselling?</h3>
  <div class="thumb b" style="left:346px;top:697px" role="img" aria-label="Photo of a counsellor holding hands with a young woman"></div>
  <h3 style="left:78px;top:847px">How to access Counselling Services</h3>
  <div class="thumb c" style="left:74px;top:877px" role="img" aria-label="Photo of a hand typing on a laptop keyboard"></div>
  <h3 style="left:350px;top:847px">How will it help me?</h3>
  <div class="thumb d" style="left:346px;top:877px" role="img" aria-label="Photo of a group of smiling children giving thumbs up"></div>
</div>

<aside class="side">
  <h2 style="left:627px;top:450px">Latest News</h2>
  <div class="side-box" style="top:478px;height:240px">
    <ul>
      <li>Aliquam vulputate accumsan. Ves tibulum aliquet ultricies tortor.<time>Aug-3-13</time></li>
      <li>Aliquam vulputate accumsan. Ves tibulum aliquet ultricies tortor.<time>Aug-3-13</time></li>
      <li>Aliquam vulputate accumsan. Ves tibulum aliquet ultricies tortor.<time>Aug-3-13</time></li>
    </ul>
    <div class="view-all">View all</div>
  </div>
  <h2 style="left:627px;top:734px">Latest Events</h2>
  <div class="side-box" style="top:763px;height:240px">
    <ul>
      <li>Aliquam vulputate accumsan. Ves tibulum aliquet ultricies tortor.<time>Aug-3-13</time></li>
      <li>Aliquam vulputate accumsan. Ves tibulum aliquet ultricies tortor.<time>Aug-3-13</time></li>
      <li>Aliquam vulputate accumsan. Ves tibulum aliquet ultricies tortor.<time>Aug-3-13</time></li>
    </ul>
    <div class="view-all">View all</div>
  </div>
</aside>

<footer class="abs footer">
  <div class="footer-col" style="left:24px"><h4>Quick Links</h4><ul><li>Suspendisse</li><li>Donec fringilla</li><li>Proin eget</li><li>Svenenatis</li></ul></div>
  <div class="footer-col" style="left:157px"><h4>Quick Links</h4><ul><li>Suspendisse</li><li>Donec fringilla</li><li>Proin eget</li><li>Svenenatis</li></ul></div>
  <div class="footer-col" style="left:290px"><h4>Quick Links</h4><ul><li>Suspendisse</li><li>Donec fringilla</li><li>Proin eget</li><li>Svenenatis</li></ul></div>
  <div class="footer-col" style="left:424px"><h4>Quick Links</h4><ul><li>Suspendisse</li><li>Donec fringilla</li><li>Proin eget</li><li>Svenenatis</li></ul></div>
  <div class="footer-col" style="left:573px"><h4>Newsletter Sign up</h4></div>
  <div class="email">Email ID<span class="arrow"><svg width="20" height="20" viewBox="0 0 20 20"><path d="M8 5l5 5-5 5" fill="none" stroke="#222" stroke-width="2"/></svg></span></div>
  <div class="social"><i class="s1"></i><i class="s2"></i><i class="s3"></i><i class="s4"></i></div>
</footer>
<div class="abs copyright">Copyright&nbsp; ©&nbsp; 2013&nbsp; Willowmere Care.&nbsp;&nbsp; All rights reserved.</div>
</body>
</html>
```